Veltrona Services

Double sided business cards with color on front and black and white on back. I have basic ideas and graphics, but am looking for someone to take them to the next level

```html
<!DOCTYPE html>
<html lang="en">
<head>
<meta charset="utf-8">
<title>Veltrona Services – Business Card</title>
<link href="https://fonts.googleapis.com/css2?family=Arimo:wght@400;700&family=Montserrat:wght@700&display=swap" rel="stylesheet">
<style>
  :root {
    --backdrop: #e9e9e8;
    --card: #ffffff;
    --brand-green: #6cbf3a;
    --ink: #3a3a3a;
    --ink-soft: #555555;
    --rule: #6b6b6b;
    --emblem: #000000;
    --tagline: #444444;
  }
  * { box-sizing: border-box; margin: 0; padding: 0; }
  html, body {
    width: 1200px; height: 802px; overflow: hidden;
    background: var(--backdrop);
    font-family: "Arimo", Arial, sans-serif;
  }
  .sheet {
    position: relative; width: 1200px; height: 802px;
    display: flex; align-items: center; justify-content: center; gap: 60px;
  }
  .card {
    width: 520px; height: 297px; background: var(--card);
    box-shadow: 0 6px 18px rgba(0,0,0,0.12);
    position: relative;
  }

  /* Front side */
  .card-front { display: flex; align-items: center; }
  .brand-block {
    width: 230px; display: flex; flex-direction: column; align-items: center; gap: 14px;
  }
  .brand-dot {
    width: 64px; height: 64px; border-radius: 50%;
    background: var(--brand-green);
  }
  .brand-name {
    font-family: "Montserrat", Arial, sans-serif; font-weight: 700;
    font-size: 18px; letter-spacing: 0.5px; text-transform: uppercase;
    color: var(--brand-green); text-align: center; line-height: 1.2;
  }
  .divider { width: 1.5px; height: 120px; background: var(--rule); }
  .contact-block { padding-left: 22px; color: var(--ink); }
  .person-name {
    font-weight: 700; font-size: 18px; letter-spacing: 0.5px;
    color: var(--brand-green); text-transform: uppercase;
  }
  .person-role { font-size: 13px; color: var(--ink-soft); margin: 3px 0 10px; }
  .address { font-size: 13px; line-height: 1.35; margin-bottom: 8px; }
  .contact-line { display: flex; align-items: center; gap: 7px; font-size: 13px; line-height: 1.5; }
  .contact-icon { width: 12px; height: 12px; flex: none; }

  /* Back side */
  .card-back {
    display: flex; flex-direction: column; align-items: center; justify-content: center;
  }
  .emblem-row { display: flex; align-items: center; gap: 14px; margin-bottom: 34px; }
  .emblem-circle {
    width: 70px; height: 70px; border-radius: 50%; background: var(--emblem);
  }
  .emblem-name {
    font-family: "Arimo", Arial, sans-serif; font-weight: 700;
    font-size: 20px; letter-spacing: 0.5px; text-transform: uppercase; color: var(--emblem);
  }
  .tagline {
    font-weight: 700; font-size: 15px; text-transform: uppercase; text-align: center;
    line-height: 1.3; letter-spacing: 0.3px; color: var(--tagline);
  }
</style>
</head>
<body>
<main class="sheet">
  <section class="card card-front" aria-label="Card front">
    <div class="brand-block">
      <div class="brand-dot"></div>
      <div class="brand-name">Veltrona Services</div>
    </div>
    <div class="divider"></div>
    <div class="contact-block">
      <div class="person-name">Marcus Ellery</div>
      <div class="person-role">Manager</div>
      <div class="address">Your Address, City<br>State, Zip 0000</div>
      <div class="contact-line">
        <svg class="contact-icon" viewBox="0 0 12 12"><circle cx="6" cy="6" r="6" fill="var(--brand-green)"/><path d="M3.6 3.2 L5 3 L5.5 4.6 L4.7 5.2 Q5.4 6.7 6.8 7.3 L7.4 6.5 L9 7 L8.8 8.4 Q5.6 8.8 3.6 5.2 Z" fill="#fff"/></svg>
        <span>555-014-2287</span>
      </div>
      <div class="contact-line">
        <svg class="contact-icon" viewBox="0 0 12 12"><rect x="0.5" y="2" width="11" height="8" rx="1" fill="var(--brand-green)"/><path d="M1 2.6 L6 6.6 L11 2.6" stroke="#fff" stroke-width="1" fill="none"/></svg>
        <span>hello@veltronamail.com</span>
      </div>
      <div class="contact-line">
        <svg class="contact-icon" viewBox="0 0 12 12"><circle cx="6" cy="6" r="6" fill="var(--brand-green)"/><circle cx="6" cy="6" r="3.8" fill="none" stroke="#fff" stroke-width="0.9"/><path d="M2.2 6 H9.8 M6 2.2 V9.8" stroke="#fff" stroke-width="0.9"/></svg>
        <span>www.veltronaservices.com</span>
      </div>
    </div>
  </section>

  <section class="card card-back" aria-label="Card back">
    <div class="emblem-row">
      <div class="emblem-circle"></div>
      <div class="emblem-name">Veltrona Services</div>
    </div>
    <p class="tagline">
      A Thoughtful Approach<br>
      Every Detail Handled With Care
    </p>
  </section>
</main>
</body>
</html>
```